Restaurant Finder Website Design

I need to create a website that will help people find restaurants around a zip code or address.

I would like to have a very clean and simple design. I will need a design for the homepage, that should be very clean and simple to use. its where the users will launch their search. I am thinking something like pomira like.. big search field with a very clean page where users can create an account or restaurants subscribe to the service.

Also need the design of the search results page, I would like to display a big map with the results and a list on the side or the bottom of the map.

Also need a profile page for the users that sign up to the site.

Mostly what I need are guidelines and color coordinated elements, like a general layout and buttons that work together. I would like to know what the action buttons and elements should look like. Because its going to have some more detail pages.

Target Market(s)

People in general, mainly people that work at an office and have to find a place for lunch every day.

Industry/Entity Type

Restaurant

Number of Pages Required

4 page

Font styles to use
Serif
Sans Serif

Requirements
Must have
• It must be a really simple and clean design but look edgy.

```html
<!DOCTYPE html>
<html lang="en">
<head>
<meta charset="utf-8">
<title>ForkNear – Restaurant Finder</title>
<link href="https://fonts.googleapis.com/css2?family=Poppins:wght@300;400;500;600&display=swap" rel="stylesheet">
<style>
:root{
  --red:#d0202a;
  --dark:#3a3a3a;
  --text:#444;
  --muted:#888;
  --line:#e4e4e4;
  --soft:#f7f7f7;
  --footer:#efefef;
  --star:#f5a623;
}
*{margin:0;padding:0;box-sizing:border-box}
html,body{width:1200px;height:1200px;overflow:hidden;background:#fff;font-family:'Poppins',sans-serif;color:var(--text)}
.page{position:absolute;left:305.6px;top:0;width:736px;height:1500px;transform:scale(.8);transform-origin:0 0;background:#fff}
.abs{position:absolute}
/* top bar */
.topbar{left:0;top:0;width:736px;height:20px;background:var(--dark);color:#fff;font-size:7px}
.topbar .phone{left:55px;top:5px}
.topbar .phone b{color:var(--red);font-weight:400}
.topbar .acct{left:530px;top:5px}
.topbar .social{left:624px;top:3px;display:flex;gap:3px}
.topbar .social i{width:13px;height:13px;border-radius:50%;background:#888;display:block}
/* nav */
.nav{left:0;top:20px;width:736px;height:38px;background:#fff}
.brand{display:flex;align-items:center;gap:6px;font-size:11px;font-weight:500;color:#222}
.brand i{width:18px;height:18px;border-radius:50%;background:var(--red);display:block}
.nav .brand{left:55px;top:9px}
.nav ul{list-style:none;left:354px;top:17px;display:flex;font-size:7px;color:#555}
.nav li{margin-right:12px}
.nav li+li:before{content:"|";margin-right:12px;color:#999}
.cart{left:649px;top:13px;width:37px;height:15px;background:var(--red)}
.cart span{position:absolute;right:0;top:0;width:12px;height:15px;background:#f5b223;color:#fff;font-size:7px;text-align:center;line-height:15px}
/* hero */
.hero{left:0;top:58px;width:736px;height:252px;background:radial-gradient(ellipse at 30% 40%,#7a4a2c 0%,#4a2a1b 45%,#2a1810 100%)}
.hero h1{position:absolute;top:40px;width:100%;text-align:center;color:#fff;font-size:21px;font-weight:400;letter-spacing:.5px}
.field{width:173px;height:29px;background:#fff;font-size:9px;color:#aaa;display:flex;align-items:center;padding-left:30px}
.field:after{content:"";position:absolute;right:10px;top:11px;border:5px solid transparent;border-top:7px solid #555}
.field .ic{position:absolute;left:9px;top:8px;width:13px;height:13px;border:1.5px solid #999;border-radius:3px}
.find{width:173px;height:29px;background:var(--red);color:#fff;font-size:9px;font-weight:500;text-align:center;line-height:29px}
/* results */
.sec-title{width:736px;text-align:center;color:var(--red);font-size:16px;font-weight:400}
.sec-sub{width:736px;text-align:center;color:#666;font-size:8.5px}
.map{left:55px;top:408px;width:331px;height:516px;background:linear-gradient(135deg,#eae6d8 0%,#dde6cf 50%,#e8e2cf 100%)}
.list-head{left:397px;top:407px;font-size:11.5px;color:#555}
.card{left:397px;width:289px;height:76px;border:1px solid var(--line);background:#fff}
.card .thumb{position:absolute;left:10px;top:10px;width:76px;height:53px;background:linear-gradient(180deg,#7a0e10 0%,#3a0c0a 55%,#8a5a2a 100%)}
.card h3{position:absolute;left:95px;top:10px;font-size:8.5px;font-weight:400;color:#333}
.card p{position:absolute;left:95px;top:23px;width:180px;font-size:6px;line-height:8px;color:#999}
.card .stars{position:absolute;left:224px;top:9px;color:var(--star);font-size:9px;letter-spacing:-1px}
.card .more{position:absolute;left:224px;top:49px;width:41px;height:13px;background:var(--red);color:#fff;font-size:4.8px;text-align:center;line-height:13px}
/* how it works */
.how{left:0;top:924px;width:736px;height:290px;background:var(--soft)}
.step{width:120px;text-align:center;font-size:9.5px;line-height:11px;color:#555}
/* banner */
.banner{left:54px;top:1228px;width:630px;height:98px;background:linear-gradient(90deg,#2f2a26 0%,#4c4036 55%,#6a5a48 80%,#d8d2c6 100%)}
.banner h2{position:absolute;left:44px;top:30px;color:#fff;font-size:14px;font-weight:400}
.banner p{position:absolute;left:44px;top:49px;width:260px;color:#fff;font-size:6.8px;line-height:8px}
.order{left:352px;top:39px;width:104px;height:25px;background:var(--red);color:#fff;font-size:9px;text-align:center;line-height:25px}
/* footer */
.footer{left:0;top:1362px;width:736px;height:138px;background:var(--footer);font-size:6.5px;color:#666}
.footer h4{font-size:7.5px;font-weight:500;color:#333}
.footer .brand{left:55px;top:18px;font-size:12px}
.footer .brand i{width:22px;height:22px}
.footer ul{list-style:none;line-height:11px}
.footer li:before{content:"› ";color:var(--red)}
.footer .copy{left:55px;top:115px;font-size:6px;color:#999}
.footer .rule{left:0;top:105px;width:736px;height:1px;background:#ddd}
.email{left:586px;top:112px;width:74px;height:18px;background:#fff;border:1px solid #ddd;font-size:6px;color:#bbb;padding:5px 6px}
.send{left:660px;top:112px;width:26px;height:18px;background:var(--red)}
</style>
</head>
<body>
<div class="page">
  <div class="abs topbar">
    <div class="abs phone">&#9990; +100 20000 200 <b>FREE</b></div>
    <div class="abs acct">Login &nbsp;|&nbsp; Sign Up</div>
    <div class="abs social"><i></i><i></i><i></i><i></i></div>
  </div>

  <header class="abs nav">
    <div class="abs brand"><i></i>ForkNear</div>
    <ul class="abs"><li>HOME</li><li>MENU</li><li>FUNDRAISING</li><li>ABOUT</li><li>CONTACT</li></ul>
    <svg class="abs" style="left:628px;top:16px" width="10" height="10" viewBox="0 0 10 10"><circle cx="4" cy="4" r="3" fill="none" stroke="#d0202a" stroke-width="1.3"/><line x1="6.2" y1="6.2" x2="9" y2="9" stroke="#d0202a" stroke-width="1.3"/></svg>
    <div class="abs cart"><svg class="abs" style="left:5px;top:3px" width="14" height="10" viewBox="0 0 14 10"><path d="M0 1h3l2 6h7l1-4H4" fill="none" stroke="#fff" stroke-width="1"/><circle cx="6" cy="9" r="1" fill="#fff"/><circle cx="11" cy="9" r="1" fill="#fff"/></svg><span>2</span></div>
  </header>

  <section class="abs hero" role="img" aria-label="Overhead photo of a table of tacos, grilled meat and fresh vegetables">
    <h1>CATEGORIES</h1>
    <div class="abs field" style="left:189px;top:94px"><span class="ic" style="border-radius:50% 50% 50% 0"></span>Select By Location</div>
    <div class="abs field" style="left:373px;top:94px"><span class="ic" style="border-radius:50%"></span>Select By Food</div>
    <div class="abs field" style="left:189px;top:135px"><span class="ic"></span>By Price Range</div>
    <div class="abs find" style="left:373px;top:135px">FIND IT NOW
      <svg class="abs" style="right:10px;top:10px" width="9" height="9" viewBox="0 0 10 10"><circle cx="4" cy="4" r="3" fill="none" stroke="#fff" stroke-width="1.5"/><line x1="6.2" y1="6.2" x2="9" y2="9" stroke="#fff" stroke-width="1.5"/></svg></div>
    <svg class="abs" style="left:359px;top:205px" width="16" height="26" viewBox="0 0 16 26"><rect x="1" y="1" width="14" height="24" rx="7" fill="none" stroke="#fff" stroke-width="1.3"/><line x1="8" y1="6" x2="8" y2="11" stroke="#fff" stroke-width="1.3"/></svg>
  </section>

  <div class="abs sec-title" style="top:342px">LOREM IPSUM SIMPLE DUMMY</div>
  <div class="abs sec-sub" style="top:366px">Lorem Ipsum Simple Dummy Content Provide lorem Ipsum Simle</div>

  <div class="abs map" role="img" aria-label="Street map of the city with red restaurant markers"></div>
  <div class="abs list-head">LOREM IPSUM SIMPLE DUMMY CONTENT</div>

  <div class="abs card" style="top:431px"><div class="thumb" role="img" aria-label="Restaurant storefront at night"></div><h3>LOREM IPSUM SIMPLE</h3><span class="stars">★★★★★</span><p>Lorem ipsum dolor sit amet, consectetuer adipiscing elit, euismod tincidunt ut</p><span class="more">READ MORE</span></div>
  <div class="abs card" style="top:514.5px"><div class="thumb" role="img" aria-label="Restaurant storefront by day" style="background:linear-gradient(180deg,#5a5a6a 0%,#8a1a1a 50%,#2a2a2a 100%)"></div><h3>LOREM IPSUM SIMPLE</h3><span class="stars">★★★★★</span><p>Lorem ipsum dolor sit amet, consectetuer adipiscing elit, euismod tincidunt ut</p><span class="more">READ MORE</span></div>
  <div class="abs card" style="top:598px"><div class="thumb" role="img" aria-label="Restaurant storefront at night"></div><h3>LOREM IPSUM SIMPLE</h3><span class="stars">★★★★★</span><p>Lorem ipsum dolor sit amet, consectetuer adipiscing elit, euismod tincidunt ut</p><span class="more">READ MORE</span></div>
  <div class="abs card" style="top:681.5px"><div class="thumb" role="img" aria-label="Restaurant storefront at night"></div><h3>LOREM IPSUM SIMPLE</h3><span class="stars">★★★★★</span><p>Lorem ipsum dolor sit amet, consectetuer adipiscing elit, euismod tincidunt ut</p><span class="more">READ MORE</span></div>
  <div class="abs card" style="top:765px"><div class="thumb" role="img" aria-label="Restaurant storefront at night"></div><h3>LOREM IPSUM SIMPLE</h3><span class="stars">★★★★★</span><p>Lorem ipsum dolor sit amet, consectetuer adipiscing elit, euismod tincidunt ut</p><span class="more">READ MORE</span></div>
  <div class="abs card" style="top:848.5px"><div class="thumb" role="img" aria-label="Restaurant storefront at night"></div><h3>LOREM IPSUM SIMPLE</h3><span class="stars">★★★★★</span><p>Lorem ipsum dolor sit amet, consectetuer adipiscing elit, euismod tincidunt ut</p><span class="more">READ MORE</span></div>

  <section class="abs how">
    <div class="abs sec-title" style="top:52px">HOW IT WORKS</div>
    <div class="abs sec-sub" style="top:77px">Lorem Ipsum Simple Dummy Content Provide lorem Ipsum Simle</div>
    <svg class="abs" style="left:0;top:0" width="736" height="290" viewBox="0 0 736 290">
      <path d="M78 196 C120 180 140 176 148 174 M224 165 L267 164 M343 170 L388 186 M468 190 L510 188 M588 170 C620 160 640 140 652 128" fill="none" stroke="#bbb" stroke-width="3" stroke-dasharray="6 4"/>
      <polygon points="646,122 667,121 664,142" fill="#d0202a"/>
      <g fill="#fff" stroke="#d0202a" stroke-width="2">
        <circle cx="186" cy="174" r="38"/><circle cx="305" cy="174" r="38"/><circle cx="431" cy="174" r="38"/><circle cx="550" cy="174" r="38"/>
      </g>
      <g fill="none" stroke="#888" stroke-width="2">
        <path d="M186 190 C176 176 174 170 174 164 a12 12 0 0 1 24 0 c0 6 -2 12 -12 26z"/><circle cx="186" cy="164" r="4"/><path d="M172 186 l-6 8 h40 l-6 -8"/>
        <circle cx="305" cy="174" r="19"/><line x1="305" y1="155" x2="305" y2="193"/><line x1="286" y1="174" x2="324" y2="174"/>
        <rect x="416" y="158" width="24" height="30" rx="2"/><rect x="424" y="168" width="20" height="13" fill="#fff"/><line x1="421" y1="164" x2="434" y2="164"/>
        <circle cx="550" cy="165" r="9"/><path d="M532 193 c0 -12 8 -17 18 -17 s18 5 18 17z"/>
      </g>
    </svg>
    <div class="abs step" style="left:126px;top:232px">Select Your<br>Location</div>
    <div class="abs step" style="left:245px;top:232px">Select Your<br>Food</div>
    <div class="abs step" style="left:371px;top:232px">ChoosePrice<br>Range</div>
    <div class="abs step" style="left:490px;top:232px">Enjoy Your<br>Food</div>
  </section>

  <section class="abs banner" role="img" aria-label="Photo of takeaway dishes on a dark table with a plated salad">
    <h2>LOREM IPSUM SIMPLE DUMMY</h2>
    <p>Lorem Ipsum is simply dummy text of the printing and typesetting industry. Lorem Ipsum has been the industry's standard dummy text ever since the 1500s, when an</p>
    <div class="abs order">ORDER NOW</div>
  </section>

  <footer class="abs footer">
    <div class="abs brand"><i></i>ForkNear</div>
    <div class="abs" style="left:194px;top:17px"><h4>CONTACT INFORMATION</h4>
      <div style="margin-top:9px;line-height:11px">23 lorem ipsum simple text provide<br>Tel: (123) 555-0148<br>Email hello@forknear.example</div>
      <div style="display:flex;gap:2px;margin-top:3px"><i style="width:9px;height:9px;border-radius:50%;background:#4a90d9;display:block"></i><i style="width:9px;height:9px;border-radius:50%;background:#4a90d9;display:block"></i><i style="width:9px;height:9px;border-radius:50%;background:#4a90d9;display:block"></i><i style="width:9px;height:9px;border-radius:50%;background:#4a90d9;display:block"></i></div>
    </div>
    <div class="abs" style="left:344px;top:18px"><h4>QUICK LINKS</h4>
      <div style="display:flex;gap:28px;margin-top:8px"><ul><li>About Us</li><li>Services</li><li>Pricing</li><li>FAQ</li></ul><ul><li>Contact us</li><li>Site Map</li></ul></div>
    </div>
    <div class="abs" style="left:484px;top:18px"><h4>WE ARE OPEN</h4>
      <div style="margin-top:8px;line-height:11px">Delivery in 15 min<br>Pick-up in 20 min</div></div>
    <div class="abs" style="left:563px;top:18px;width:130px"><h4>24 HOURS, 7 DAYS</h4>
      <div style="margin-top:8px;line-height:11px">Delivery and pick-up available<br>Delivery charge: £10.00 above £100.00, not available below £100.00</div></div>
    <div class="abs rule"></div>
    <div class="abs copy">© 2016 forknear.example</div>
    <div class="abs email">Email</div>
    <div class="abs send"><svg class="abs" style="left:7px;top:4px" width="12" height="10" viewBox="0 0 12 10"><path d="M0 5 L12 0 L9 10 L6 6z" fill="none" stroke="#fff" stroke-width="1"/></svg></div>
  </footer>
</div>
</body>
</html>
```